Dolsemk Business Cards

Business cards for real estate
Target Market(s)
Real estate
Industry/Entity Type
Real Estate Agent
Font styles to use
Serif
Requirements
Must have
- Photo and logo

```html
<!DOCTYPE html>
<html lang="en">
<head>
<meta charset="utf-8">
<title>Dolsemk Realty Business Cards</title>
<link href="https://fonts.googleapis.com/css2?family=Marcellus&family=Cinzel:wght@700&family=Tinos&display=swap" rel="stylesheet">
<style>
  :root{
    --backdrop:#000;
    --paper:#ffffff;
    --maroon:#7e1f27;
    --maroon-deep:#5e141b;
    --bronze:#b07b45;
    --bronze-dark:#8a4a2c;
    --gold:#c9a063;
    --ink:#1a1a1a;
    --accent-green:#8fc04b;
    --charcoal:#151515;
  }
  *{margin:0;padding:0;box-sizing:border-box}
  html,body{width:900px;height:1200px;overflow:hidden;background:var(--backdrop)}
  .canvas{position:relative;width:900px;height:1200px}
  .card{position:absolute;left:85px;width:733px;height:429px;border-radius:22px;overflow:hidden;background:var(--paper)}
  .card--front{top:137px}
  .card--back{top:632px}
  .card svg.shapes{position:absolute;inset:0}
  .brand{position:absolute;font-family:"Marcellus",serif;color:var(--ink);line-height:1}
  .brand__name{display:block}
  .brand__sub{display:block}
  .card--front .brand{right:30px;top:68px;text-align:right}
  .card--front .brand__name{font-size:44px;letter-spacing:1px}
  .card--front .brand__sub{font-size:33px;letter-spacing:5px;margin-top:6px}
  .card--back .brand{left:260px;top:92px}
  .card--back .brand__name{font-size:58px;letter-spacing:1px}
  .card--back .brand__sub{font-size:46px;letter-spacing:7px;margin-top:8px}
  .agent{position:absolute;right:30px;top:232px;text-align:right}
  .agent__name{font-family:"Cinzel",serif;font-weight:700;font-size:20px;color:var(--paper);letter-spacing:.5px}
  .agent__title{font-family:"Tinos",serif;font-size:15px;color:var(--accent-green);margin-top:2px}
  .contact{position:absolute;right:30px;top:285px;list-style:none;text-align:right}
  .contact li{font-family:"Tinos",serif;font-size:16px;color:var(--paper);height:24px;line-height:24px;display:flex;justify-content:flex-end;align-items:center;gap:10px}
  .contact svg{width:16px;height:16px;flex:none}
  .badges{position:absolute;left:198px;top:362px;display:flex;gap:18px}
  .badge{width:38px;height:40px;border-radius:3px;background:var(--paper)}
  .website{position:absolute;left:58px;top:383px;font-family:"Tinos",serif;font-size:16px;letter-spacing:3px;color:var(--paper)}
</style>
</head>
<body>
<div class="canvas">

  <section class="card card--front">
    <svg class="shapes" width="733" height="429" viewBox="0 0 733 429">
      <defs>
        <linearGradient id="panelBronze" x1="0" y1="0" x2="1" y2="0.3">
          <stop offset="0" stop-color="#8a3f2a"/>
          <stop offset="0.55" stop-color="#b07b45"/>
          <stop offset="1" stop-color="#9a5a35"/>
        </linearGradient>
        <linearGradient id="portraitTone" x1="0" y1="0" x2="0" y2="1">
          <stop offset="0" stop-color="#e9e9ec"/>
          <stop offset="0.45" stop-color="#9a9ca4"/>
          <stop offset="1" stop-color="#2a2d36"/>
        </linearGradient>
      </defs>
      <path d="M0,0 H150 C60,40 0,110 0,110 Z" fill="var(--bronze)"/>
      <path d="M345,0 H733 V429 H0 V0 Z" fill="var(--paper)"/>
      <path d="M340,201 H733 V429 H0 V395 C150,375 290,300 340,201 Z" fill="url(#panelBronze)"/>
      <path role="img" aria-label="Portrait photo of the realtor in a dark suit" d="M0,120 C50,40 130,10 250,10 L300,10 C300,140 260,270 150,348 L0,348 Z" fill="url(#portraitTone)"/>
      <path d="M0,429 V400 C200,370 330,240 352,0 H340 C320,240 190,350 0,378 Z" fill="var(--gold)"/>
      <path d="M0,429 H90 C240,380 340,250 350,0 H336 C318,230 200,350 0,392 Z" fill="var(--maroon)"/>
      <circle cx="435" cy="105" r="55" fill="var(--maroon)"/>
    </svg>

    <div class="brand"><span class="brand__name">DOLSEMK</span><span class="brand__sub">REALTY</span></div>

    <div class="agent">
      <div class="agent__name">YOUR NAME HERE</div>
      <div class="agent__title">Realtor ®</div>
    </div>

    <ul class="contact">
      <li>0612-4470-2281
        <svg viewBox="0 0 16 16"><rect x="4" y="1" width="8" height="14" rx="1.5" fill="none" stroke="var(--accent-green)" stroke-width="1.6"/><circle cx="8" cy="12.5" r="0.9" fill="var(--accent-green)"/></svg></li>
      <li>0731-5582-9043
        <svg viewBox="0 0 16 16"><path d="M3,2 L6,2 L7,5 L5.5,6.5 C6.5,8.5 7.5,9.5 9.5,10.5 L11,9 L14,10 L14,13 C8,14 2,8 3,2 Z" fill="var(--accent-green)"/></svg></li>
      <li>info@dolsemkrealty.com
        <svg viewBox="0 0 16 16"><rect x="1" y="3.5" width="14" height="9" fill="var(--accent-green)"/><path d="M1,3.5 L8,9 L15,3.5" fill="none" stroke="var(--paper)" stroke-width="1.2"/></svg></li>
      <li>www.dolsemkrealty.com
        <svg viewBox="0 0 16 16"><circle cx="8" cy="8" r="6.5" fill="var(--accent-green)"/><path d="M1.5,8 H14.5 M8,1.5 C5,5 5,11 8,14.5 M8,1.5 C11,5 11,11 8,14.5" fill="none" stroke="var(--paper)" stroke-width="0.9"/></svg></li>
      <li>2240 Linden Row, Suite 4, Harrow Vale, MD 20990
        <svg viewBox="0 0 16 16"><path d="M8,15 C4,10 3,8 3,6 A5,5 0 0 1 13,6 C13,8 12,10 8,15 Z" fill="var(--accent-green)"/><circle cx="8" cy="6" r="1.8" fill="var(--paper)"/></svg></li>
    </ul>

    <div class="badges">
      <span class="badge"></span>
      <span class="badge"></span>
    </div>
  </section>

  <section class="card card--back">
    <svg class="shapes" width="733" height="429" viewBox="0 0 733 429">
      <defs>
        <linearGradient id="homeScene" x1="0" y1="0" x2="0" y2="1">
          <stop offset="0" stop-color="#dfe4ee"/>
          <stop offset="0.45" stop-color="#ece8e4"/>
          <stop offset="1" stop-color="#d6dfcc"/>
        </linearGradient>
        <linearGradient id="backBronze" x1="0" y1="0" x2="1" y2="0">
          <stop offset="0" stop-color="#7e1f27"/>
          <stop offset="0.5" stop-color="#a0603a"/>
          <stop offset="1" stop-color="#b07b45"/>
        </linearGradient>
      </defs>
      <rect role="img" aria-label="Soft faded photo of a suburban house with lawn" width="733" height="429" fill="url(#homeScene)"/>
      <path d="M0,348 C260,350 500,290 733,140 V429 H0 Z" fill="var(--charcoal)"/>
      <path d="M0,358 C270,360 520,300 733,156 V429 H0 Z" fill="var(--paper)"/>
      <path d="M0,366 C280,368 520,310 640,240 C560,320 480,390 440,429 H0 Z" fill="url(#backBronze)"/>
      <path d="M640,240 C690,205 715,185 733,170 V429 H470 C530,360 590,300 640,240 Z" fill="var(--charcoal)"/>
      <path d="M450,429 C540,330 640,230 733,10 V30 C660,220 560,340 470,429 Z" fill="var(--maroon)"/>
      <path d="M420,429 C520,340 620,250 733,40 V52 C630,260 530,350 440,429 Z" fill="var(--paper)"/>
      <circle cx="147" cy="146" r="80" fill="var(--maroon)"/>
    </svg>

    <div class="brand"><span class="brand__name">DOLSEMK</span><span class="brand__sub">REALTY</span></div>

    <div class="website">WWW.DOLSEMKREALTY.COM</div>
  </section>

</div>
</body>
</html>
```